Label Design for Saffron Company

We need a label design that is unique for our container. The item inside the container is Saffron, and it is 5g in weigh. We need on the label our logo, the weight and quality. Here is the exactly what we want. We want the background to be black for the label and the design to present royalty, and premium quality.

Premium Quality
Grade A+ Premium Saffron
100% Natural and Pure
www.VelmoraSpice.com

Target Market(s)

Everyone

Requirements
Must have
• Black background, golden border design. Unique design, that show premium and royalty.
Nice to have
• The logo is attached with transparent background so you can show exactly how things look like.
Should not have
• different colors that are not part of the logo.

```html
<!DOCTYPE html>
<html lang="en">
<head>
<meta charset="utf-8">
<title>Velmora Spice – Saffron Tin Label</title>
<link rel="stylesheet" href="https://fonts.googleapis.com/css2?family=Cinzel:wght@400;600;700&family=Marcellus&family=Poppins:wght@400&display=swap">
<style>
  :root {
    --page-bg: #ffffff;
    --label-black: #0d0b0a;
    --label-pattern: #1c1714;
    --gold-light: #f6e7a6;
    --gold-mid: #d4af37;
    --gold-deep: #a9791d;
    --text-white: #f4f1ea;
  }
  html, body {
    margin: 0;
    padding: 0;
    width: 1200px;
    height: 2398px;
    overflow: hidden;
    background: var(--page-bg);
  }
  .canvas {
    position: relative;
    width: 1200px;
    height: 2398px;
  }
  .label-art {
    position: absolute;
    inset: 0;
    width: 1200px;
    height: 2398px;
    display: block;
  }
  .brand-name {
    font-family: "Marcellus", "Cinzel", serif;
    fill: var(--text-white);
  }
  .headline {
    font-family: "Cinzel", serif;
    font-weight: 700;
    fill: url(#goldText);
  }
  .detail-line {
    font-family: "Poppins", sans-serif;
    font-weight: 400;
    fill: var(--text-white);
  }
  .web-address {
    font-family: "Cinzel", serif;
    font-weight: 600;
    fill: url(#goldText);
  }
</style>
</head>
<body>
<main class="canvas">
  <svg class="label-art" viewBox="0 0 1200 2398" xmlns="http://www.w3.org/2000/svg" aria-label="Velmora Spice saffron tin label">
    <defs>
      <linearGradient id="goldStroke" x1="0" y1="0" x2="1" y2="1">
        <stop offset="0" stop-color="var(--gold-light)"/>
        <stop offset="0.45" stop-color="var(--gold-mid)"/>
        <stop offset="0.75" stop-color="var(--gold-deep)"/>
        <stop offset="1" stop-color="var(--gold-light)"/>
      </linearGradient>
      <linearGradient id="goldText" x1="0" y1="0" x2="0" y2="1">
        <stop offset="0" stop-color="var(--gold-light)"/>
        <stop offset="0.55" stop-color="var(--gold-mid)"/>
        <stop offset="1" stop-color="var(--gold-deep)"/>
      </linearGradient>
      <radialGradient id="patternTone" cx="0.5" cy="0.5" r="0.5">
        <stop offset="0" stop-color="var(--label-pattern)"/>
        <stop offset="1" stop-color="var(--label-black)"/>
      </radialGradient>
      <path id="addressArc" d="M 235 1199 A 365 365 0 0 0 965 1199"/>
    </defs>

    <!-- label base -->
    <circle class="label-base" cx="600" cy="1199" r="530" fill="var(--label-black)"/>
    <circle class="label-pattern" cx="600" cy="1199" r="524" fill="url(#patternTone)"
            role="img" aria-label="Dark damask ornament pattern across the label background"/>

    <!-- frames -->
    <circle class="frame-outer" cx="600" cy="1199" r="510" fill="none" stroke="url(#goldStroke)" stroke-width="5"/>
    <circle class="frame-dots" cx="600" cy="1199" r="474" fill="none" stroke="var(--gold-mid)"
            stroke-width="7" stroke-linecap="round" stroke-dasharray="0 23"/>
    <circle class="frame-inner" cx="610" cy="1199" r="412" fill="none" stroke="url(#goldStroke)" stroke-width="3"/>

    <!-- brand mark stand-in -->
    <rect class="brand-square" x="522" y="837" width="156" height="156" rx="18"
          fill="none" stroke="url(#goldStroke)" stroke-width="4"/>
    <text class="brand-name" x="600" y="1075" font-size="46" text-anchor="middle" letter-spacing="10">VELMORA</text>
    <text class="brand-name" x="600" y="1150" font-size="46" text-anchor="middle" letter-spacing="10">SPICE</text>

    <!-- headline -->
    <text class="headline" x="600" y="1260" font-size="76" text-anchor="middle" letter-spacing="2">Premium Quality</text>

    <!-- details -->
    <text class="detail-line" x="600" y="1330" font-size="31" text-anchor="middle">GRADE A+</text>
    <text class="detail-line" x="600" y="1388" font-size="31" text-anchor="middle">PREMIUM SAFFRON</text>
    <text class="detail-line" x="600" y="1446" font-size="31" text-anchor="middle">100% NATURAL AND PURE</text>
    <text class="detail-line" x="600" y="1513" font-size="27" text-anchor="middle" fill="var(--gold-mid)">5G</text>

    <!-- web address on arc -->
    <text class="web-address" font-size="42" letter-spacing="1">
      <textPath href="#addressArc" startOffset="50%" text-anchor="middle">www.VelmoraSpice.com</textPath>
    </text>
  </svg>
</main>
</body>
</html>
```